Poster for a 100 y.o. Tennis Tournament

I would like a poster designed to promote our tennis tournament but I'd like to avoid some of the clichés like the shadow of a player serving. Just well styled text would be fine but some clever imagery would be a bonus.
Highlighting the fact our tournament has been running for over 100 years would be nice so a retro design would work. But that doesn't mean a modern design, for example a minimalist approach utilising the lines of a tennis court, wouldn't work.
Updates

Our tennis committee is now in the process of short listing and will provide an update within 48 hours.

Industry/Entity Type

Court

Requirements
Must have
• The poster must contain the following text at a minimum:
"Marbury Tennis Tournament"/"Since 1908"
"9 March - 11 March, 2013" or "9-11 March, 2013", etc
"www.marburytennis.com.au"

The poster must be reproducible in colour and black & white, or at least have an alternate for black & white.

The poster must be usable in both A3 and A4 sizes.
Nice to have
• The poster should contain the following text:
"Championship"
"Handicap"
"Seniors"
"Juniors"
Each above may be optionally succeeded by "Singles & Doubles", e.g. "Championship Singles & Doubles". It would actually be clearer if this additional text was used but would be repetitive, so alternate text "Singles & Doubles in all categories" might also be used. Alternatives for variety (with the first word the focus): "Championship Singles & Doubles", "Handicap Singles & Doubles", "Seniors 35+ & 50+", "Juniors 18&U, 14&U"

Ideally the poster will provision room for four to eight sponsors logos, preferably at the bottom, but failure to do this is not a show stopper.

The following text may also be used:
"Entries close February 24"
"Tollard Plate Weekend"

Attached is a photo of one of the old trophies. Utilisation of the curved style of the "Marbury Tennis Tournament" text would fit in with the history if the tournament.

The ability to reuse elements of the poster in a single page website used to promote the tournament would be an advantage (as it will provide consistency).

If you could have an image of a tennis ball that conveys the same energy as the clock/tyre image in the attached "Under the Glass Moon" poster, that would be cool. Or using split imagery of a wooden racquet and a modern racquet, but with some energy, would also be good. These are just ideas though and by no means essential.

I've also attached a photo of a t-shirt with a poster layout I thought looked good.

Some additional text that can be used:
"Brand new courts"
"Brindle Park, Oakhurst Tce, Marbury"
"Phone 0427 318 642"
"Prizes and Trophies"

```html
<!DOCTYPE html>
<html lang="en">
<head>
<meta charset="utf-8">
<title>Marbury Tennis Tournament — Poster</title>
<link rel="stylesheet" href="https://fonts.googleapis.com/css2?family=Russo+One&display=swap">
<style>
  :root {
    --page-bg: #ffffff;
    --court-blue: #1f72c2;
    --court-line: #4b8fd3;
    --accent-blue: #17a2e8;
    --ball-yellow: #d6e21e;
    --ink: #ffffff;
  }
  html, body {
    margin: 0;
    width: 1200px;
    height: 1200px;
    overflow: hidden;
    background: var(--page-bg);
  }
  .poster {
    position: absolute;
    left: 227px;
    top: 74px;
    width: 746px;
    height: 1052px;
    display: block;
  }
  .poster-bg { fill: var(--court-blue); }
  .court-line { stroke: var(--court-line); stroke-width: 5; fill: none; }
  .divider { fill: var(--accent-blue); }
  .sponsor-band { fill: var(--accent-blue); }
  .ball { fill: var(--ball-yellow); }
  .headline, .info {
    font-family: "Russo One", "Arial Black", sans-serif;
    fill: var(--ink);
  }
</style>
</head>
<body>
<svg class="poster" viewBox="0 0 746 1052" xmlns="http://www.w3.org/2000/svg">
  <rect class="poster-bg" x="0" y="0" width="746" height="1052"/>

  <g class="court">
    <rect class="court-line" x="24" y="30" width="696" height="996"/>
    <line class="court-line" x1="50" y1="30" x2="50" y2="1026"/>
    <line class="court-line" x1="694" y1="30" x2="694" y2="1026"/>
    <line class="court-line" x1="372" y1="30" x2="372" y2="1026"/>
    <line class="court-line" x1="24" y1="266" x2="720" y2="266"/>
    <line class="court-line" x1="24" y1="524" x2="720" y2="524"/>
    <line class="court-line" x1="24" y1="786" x2="720" y2="786"/>
  </g>

  <g class="headline">
    <text x="84" y="172" font-size="150" textLength="588" lengthAdjust="spacingAndGlyphs">MARBURY</text>
    <text x="84" y="286" font-size="144" textLength="588" lengthAdjust="spacingAndGlyphs">TENNIS</text>
    <text x="86" y="364" font-size="76" textLength="586" lengthAdjust="spacingAndGlyphs">TOURNAMENT</text>
  </g>

  <g role="img" aria-label="Three tennis balls">
    <circle class="ball" cx="115" cy="401" r="19"/>
    <circle class="ball" cx="160" cy="401" r="19"/>
    <circle class="ball" cx="205" cy="401" r="19"/>
  </g>
  <text class="info" x="252" y="415" font-size="40" textLength="244" lengthAdjust="spacingAndGlyphs">SINCE 1908</text>
  <g role="img" aria-label="Three tennis balls">
    <circle class="ball" cx="541" cy="401" r="19"/>
    <circle class="ball" cx="586" cy="401" r="19"/>
    <circle class="ball" cx="631" cy="401" r="19"/>
  </g>

  <rect class="divider" x="78" y="439" width="594" height="7"/>

  <text class="info" x="86" y="520" font-size="62" textLength="584" lengthAdjust="spacingAndGlyphs">9 - 11 MARCH 2013</text>

  <rect class="divider" x="78" y="550" width="594" height="7"/>

  <rect class="divider" x="369" y="557" width="6" height="262"/>
  <rect class="divider" x="78" y="659" width="286" height="7"/>
  <rect class="divider" x="380" y="659" width="292" height="7"/>
  <rect class="divider" x="78" y="819" width="594" height="7"/>

  <g class="info">
    <text x="78" y="604" font-size="32" textLength="270" lengthAdjust="spacingAndGlyphs">CHAMPIONSHIP</text>
    <text x="78" y="642" font-size="32" textLength="270" lengthAdjust="spacingAndGlyphs">CASH PRIZES</text>

    <text x="396" y="614" font-size="50" textLength="270" lengthAdjust="spacingAndGlyphs">HANDICAP</text>
    <text x="396" y="642" font-size="19" textLength="270" lengthAdjust="spacingAndGlyphs">(SINGLES &amp; DOUBLES)</text>

    <text x="78" y="740" font-size="52" textLength="280" lengthAdjust="spacingAndGlyphs">SENIORS</text>
    <text x="78" y="786" font-size="46" textLength="280" lengthAdjust="spacingAndGlyphs">35+ &amp; 50+</text>

    <text x="398" y="740" font-size="52" textLength="270" lengthAdjust="spacingAndGlyphs">JUNIORS</text>
    <text x="398" y="786" font-size="46" textLength="270" lengthAdjust="spacingAndGlyphs">14+U &amp; 18+U</text>
  </g>

  <text class="info" x="82" y="870" font-size="40" textLength="592" lengthAdjust="spacingAndGlyphs">www.marburytennis.com.au</text>
  <text class="info" x="182" y="926" font-size="55" textLength="384" lengthAdjust="spacingAndGlyphs">0427 318 642</text>

  <rect class="sponsor-band" x="96" y="938" width="558" height="48"/>
</svg>
</body>
</html>
```